Nobody Left the Lantern Burning - Tom Halvery - CD Cover Design Project

Single Cover for CD & Online media e.g. Tunebox Graphics
The first song release from Tom Halvery will be the track 'Nobody Left the Lantern Burning'.
For the release the single requires artwork that is eye catching, seriously professional & meets the requirements of Disc Sprout, Tunebox and also a physical copy on CD.
Track listings for CD will be:
1. Nobody Left the Lantern Burning
2. Nobody Left the Lantern Burning - Instrumental
see details in this link:
http://members.discsprout-example.com/faq.aspx
http://selfmadesound.discsprout-example.com/2009/11/avoid-album-art-atrocities/
http://answers.quorvex-example.com/question/index?qid=20111015141433AAdDTmH
Any advice on this would be greatly appreciated,
I would also like the two logo's I have uploaded to be used,
one is the Tom Halvery logo and the other is for Milbrook & Tandy Records logo (please remove the R and replace with a C for copyright.)
There are four high res photo shopped pictures of Tom Halvery and another zip file of many others, it would be nice to include one of these maybe on the 2nd page or back of the CD. Please don't use them as the front cover.
I imagine an Art Deco illustration but please listen to the track and let it inspire you.
Good Luck
Updates
I don't feel this is what I'm looking for, the design needs to refelct a broken heart without being a picture of a broken heart
Reason: No design has been what we are after so far so the deadline has been extended and the budget increased.

```html
<!DOCTYPE html>
<html lang="en">
<head>
<meta charset="utf-8">
<title>Nobody Left the Lantern Burning – Tom Halvery</title>
<link rel="stylesheet" href="https://fonts.googleapis.com/css2?family=IM+Fell+Double+Pica&family=Alike&display=swap">
<style>
  :root {
    --kraft: #c2a96a;
    --kraft-light: #cdb679;
    --kraft-dark: #a78f52;
    --fold-line: #3b3323;
    --title-white: #fbf8ee;
    --title-shadow: rgba(60, 45, 15, 0.55);
    --heart-red: #d9231c;
    --heart-deep: #9c120e;
    --portrait-light: #d7c3b0;
    --portrait-dark: #6c5442;
    --label-ink: #2a2218;
  }
  * { margin: 0; padding: 0; box-sizing: border-box; }
  html, body { width: 1200px; height: 1200px; overflow: hidden; }
  body { background: var(--kraft); }

  .cover {
    position: relative;
    width: 1200px;
    height: 1200px;
    overflow: hidden;
    background:
      radial-gradient(ellipse at 30% 25%, var(--kraft-light) 0%, transparent 60%),
      radial-gradient(ellipse at 80% 85%, var(--kraft-dark) 0%, transparent 55%),
      var(--kraft);
  }

  .envelope-folds { position: absolute; inset: 0; z-index: 1; }

  .heart {
    position: absolute;
    z-index: 2;
    left: 408px;
    top: 464px;
    width: 336px;
    height: 304px;
    background: radial-gradient(ellipse at 40% 35%, var(--heart-red) 0%, var(--heart-deep) 100%);
    border-radius: 45% 45% 50% 50%;
  }

  .portrait {
    position: absolute;
    z-index: 3;
    left: 824px;
    top: 700px;
    width: 376px;
    height: 500px;
    background: linear-gradient(160deg, var(--portrait-light) 0%, var(--portrait-dark) 100%);
  }

  .title { position: absolute; inset: 0; z-index: 4; font-weight: 400; }

  .title-line, .byline {
    position: absolute;
    z-index: 4;
    color: var(--title-white);
    font-family: "IM Fell Double Pica", "Alike", serif;
    font-weight: 400;
    text-shadow: 3px 4px 6px var(--title-shadow);
    white-space: nowrap;
    line-height: 1;
  }
  .title-first { left: 96px;  top: 80px;  font-size: 176px; }
  .title-key   { left: 352px; top: 284px; font-size: 184px; text-transform: uppercase; }
  .title-small { left: 448px; top: 632px; font-size: 104px; }
  .title-last  { left: 76px;  top: 722px; font-size: 138px; }
  .byline      { left: 112px; top: 1082px; font-size: 98px; }

  .label-mark, .artist-mark {
    position: absolute;
    z-index: 5;
    display: flex;
    align-items: center;
    gap: 8px;
    font-family: "Alike", serif;
    font-size: 18px;
    line-height: 1.1;
    color: var(--label-ink);
  }
  .label-mark  { left: 930px;  top: 40px; width: 150px; }
  .artist-mark { left: 1100px; top: 40px; width: 92px; }
  .mark-square {
    flex: none;
    width: 14px;
    height: 14px;
    background: var(--label-ink);
  }
</style>
</head>
<body>
  <main class="cover">
    <svg class="envelope-folds" width="1200" height="1200" viewBox="0 0 1200 1200" aria-hidden="true">
      <line x1="20" y1="0" x2="1200" y2="1040" stroke="var(--fold-line)" stroke-width="2.5"/>
      <line x1="1180" y1="0" x2="0" y2="1150" stroke="var(--fold-line)" stroke-width="2.5"/>
    </svg>

    <div class="heart" role="img" aria-label="Red heart illustration with a crack running across it"></div>

    <div class="portrait" role="img" aria-label="Photograph of the artist seated, holding a pen over an open notebook"></div>

    <div class="label-mark"><span class="mark-square"></span><span>Milbrook &amp; Tandy Records</span></div>
    <div class="artist-mark"><span>Tom Halvery</span></div>

    <h1 class="title">
      <span class="title-line title-first">Nobody</span>
      <span class="title-line title-key">Left</span>
      <span class="title-line title-small">the</span>
      <span class="title-line title-last">Lantern Burning</span>
    </h1>

    <p class="byline">– Tom Halvery</p>
  </main>
</body>
</html>
```